Business Card Design

We currently have a business card design for our main business 'Lantern Wallcover"
We are reasonably happy with our current design for Lantern Wallcover business card (black damask patterned wallpaper in background white simplistic font with white chandelier (see logo on website). www.lanternwallcover.com.au

We are considering whether its in our best interest to have a separate business card OR a double sided card to promote our secondary business 'Quill Glow'. We are open to either a double-sided card with one business on each side OR a double sided card for each business. With contact info on the back of each.

We need a new snazzy design for 'Quill Glow' our custom made lampshades from which we craft from our wallpaper designs. We had an idea that we could use the top swatch shown on this link below as the pattern in the background (Orange/black) geometric triangles.
http://www.lanternwallcover.com.au/product_info.php?products_id=1086

For the quill glow Font we would be happy with something similar to Lantern Wallcover but perhaps a little more handmade/arty slant.
Below another link shows you a few of our lampshades
http://www.lanternwallcover.com.au/index.php?cPath=10

For Quill Glow I think we also need the quote under in smaller font
"Custom-Made Wallpaper Lampshades"

Target Market(s)

Quill Glow will be for the Young Funky Apartment Dwellers, Young Families Styling Home Decor and Kids Rooms. It also attracts small business owners doing shop-fits.

Industry/Entity Type

Business

Contact Information for Business Card

We need to incorporate our sister business to the back side of our business card. I am also open to having two different business cards if designers think this will not be possible.
We need the same contact info, different logo.
ABN: 47 302 916 854
Email: sales@lanternwallcover.com.au
Postal Address: PO Box 793, Larkfield VIC 3389
Website: http://www.lanternwallcover.com.au

Requirements
Must have
• A hand-made arty appeal for Quill Glow
Was unable to get sliders to work for the look and feel so below is the best list from the above:
Bold, Playful, Modern, Personable, Colorful, Upmarket.
Nice to have
• We love the bold contrasting colors. Colors chosen for our website were Orange, Blue and Duck Egg Bright Blue!

```html
<!DOCTYPE html>
<html lang="en">
<head>
<meta charset="UTF-8">
<title>Quill Glow — Business Card</title>
<link href="https://fonts.googleapis.com/css2?family=Handlee&display=swap" rel="stylesheet">
<style>
  :root {
    --card-bg: #ffffff;
    --tone-pink: #e0458f;
    --tone-hotpink: #e8237a;
    --tone-lime: #c4cc2a;
    --tone-orange: #ef7d2d;
    --tone-charcoal: #3a3434;
    --tone-grey: #7d7576;
    --tone-cream: #ece9e0;
    --type-white: #ffffff;
    --type-shadow: rgba(40, 20, 30, 0.75);
  }
  html, body {
    margin: 0;
    padding: 0;
    width: 1200px;
    height: 741px;
    overflow: hidden;
    background: var(--card-bg);
  }
  .card {
    position: relative;
    width: 1200px;
    height: 741px;
    background: var(--card-bg);
  }
  .pattern-field {
    position: absolute;
    left: 49px;
    top: 49px;
    width: 1113px;
    height: 649px;
    background:
      linear-gradient(115deg,
        var(--tone-lime) 0%,
        var(--tone-orange) 14%,
        var(--tone-hotpink) 28%,
        var(--tone-charcoal) 42%,
        var(--tone-cream) 54%,
        var(--tone-pink) 66%,
        var(--tone-grey) 78%,
        var(--tone-lime) 90%,
        var(--tone-pink) 100%);
  }
  .brand-name,
  .tagline {
    position: absolute;
    margin: 0;
    font-family: 'Handlee', cursive;
    font-weight: 400;
    color: var(--type-white);
    text-shadow: 2px 3px 4px var(--type-shadow);
    white-space: nowrap;
  }
  .brand-name {
    left: 300px;
    top: 395px;
    font-size: 112px;
    line-height: 1;
    letter-spacing: 4px;
  }
  .tagline {
    left: 150px;
    top: 560px;
    font-size: 44px;
    line-height: 1;
    letter-spacing: 1px;
  }
</style>
</head>
<body>
  <main class="card">
    <div class="pattern-field" role="img" aria-label="Geometric wallpaper pattern of pink, lime, orange, charcoal, grey and cream triangles"></div>
    <h1 class="brand-name">Quill Glow</h1>
    <p class="tagline">Custom-Made Wallpaper Lampshades</p>
  </main>
</body>
</html>
```